Sports Nutrition Supplement Label design

We need a sports supplement label design for an existing business. (I have provided our business logo in the file uploads) These labels will remain consistent across the product line with the name of the product being the only changing field. The current product names (example: "vegan") on the labels provided are just for reference, the ingredients portions etc are final, but the actual name will be changed to something less generic for each product. I will just need to be able to change the name and have it match with label concept. We would like the look to be professional, clean, and exemplify quality. Please reference our business website tidelinevigor.com to get a feel for design and brand association.
I have also included the NKB supplement label guidelines so we are certain to maintain compliance.
Thank you and I'm looking forward to working with you and seeing your creative designs!
Darin

Target Market(s)

Athletes, Sports professionals, Colleges, Professional Sports Teams

Industry/Entity Type

Sports Science/ Sports Training/Athletics

Requirements
Nice to have
• I would like the design to possibly reflect these key terms: Sport Science, Chemistry, Clean, Professional, Quality (We also like water/ocean/waves concepts but is not a "requirement" it would have to really work well in the design somehow to appeal to wide range of athletes)

```html
<!DOCTYPE html>
<html lang="en">
<head>
<meta charset="utf-8">
<title>Tideline Vigor – Vegan Label</title>
<link rel="stylesheet" href="https://fonts.googleapis.com/css2?family=Open+Sans:wght@400;600;700;800&family=Fira+Sans+Condensed:wght@700&display=swap">
<style>
  :root {
    --brand-green: #1f8c3b;
    --brand-green-light: #5cbd82;
    --ink: #1c1c1c;
    --ink-soft: #444;
    --cocoa: #8a5a2e;
    --cocoa-light: #b98852;
    --paper: #f6f6f6;
    --paper-shade: #e4e4e4;
    --dot-tint: #d7eadc;
    --vit-blue: #1d4fb8;
    --vit-navy: #1b2f8f;
    --vit-sky: #2ea8e0;
    --vit-green: #3c9b2f;
  }
  * { margin: 0; padding: 0; box-sizing: border-box; }
  html, body {
    width: 1200px; height: 1200px; overflow: hidden;
    background: #ffffff;
    font-family: "Open Sans", sans-serif;
  }
  .label {
    position: absolute; left: 85px; top: 25px;
    width: 1030px; height: 1150px; overflow: hidden;
    background: linear-gradient(90deg, var(--paper-shade) 0%, var(--paper) 20%, #ffffff 50%, var(--paper) 80%, var(--paper-shade) 100%);
  }
  .texture-field {
    position: absolute; left: 0; right: 0; top: 640px; height: 440px;
    background: linear-gradient(180deg, rgba(215,234,220,0) 0%, var(--dot-tint) 100%);
  }
  .brand-tab {
    position: absolute; left: 194px; top: 24px; width: 640px; height: 376px;
    border-radius: 0 0 56px 56px;
    background: linear-gradient(90deg, var(--brand-green-light) 0%, var(--brand-green) 45%, var(--brand-green) 75%, var(--brand-green-light) 100%);
    display: flex; align-items: center; justify-content: center;
  }
  .brand-name {
    color: #ffffff; font-weight: 600; font-size: 60px; letter-spacing: 6px;
  }
  .vitamin {
    position: absolute; border-radius: 50%;
    display: flex; align-items: center; justify-content: center;
    color: #fff; font-weight: 800;
  }
  .vitamin-a { left: 26px; top: 182px; width: 84px; height: 98px; font-size: 46px; background: radial-gradient(circle at 35% 30%, #6fa6f0, var(--vit-blue) 60%); }
  .vitamin-fe { left: 928px; top: 180px; width: 80px; height: 96px; font-size: 40px; background: radial-gradient(circle at 35% 30%, #4a63d0, var(--vit-navy) 60%); }
  .vitamin-e { left: 6px; top: 462px; width: 44px; height: 76px; font-size: 30px; background: radial-gradient(circle at 35% 30%, #8fd6f5, var(--vit-sky) 60%); }
  .vitamin-b { left: 978px; top: 522px; width: 44px; height: 76px; font-size: 30px; background: radial-gradient(circle at 35% 30%, #86cf72, var(--vit-green) 60%); }
  .product-name {
    position: absolute; left: 0; right: 0; top: 440px; text-align: center;
    font-weight: 800; font-size: 250px; line-height: 1; letter-spacing: -6px;
    color: var(--ink-soft);
  }
  .athlete-figure {
    position: absolute; left: 4px; top: 680px; width: 76px; height: 356px;
    background: linear-gradient(180deg, var(--brand-green) 0%, var(--brand-green-light) 100%);
    border-radius: 36px 36px 10px 10px;
  }
  .flavor {
    position: absolute; left: 0; right: 0; top: 782px; text-align: center;
    font-family: "Fira Sans Condensed", sans-serif; font-weight: 700; font-size: 72px;
    background: linear-gradient(180deg, var(--cocoa-light), var(--cocoa));
    -webkit-background-clip: text; background-clip: text; color: transparent;
  }
  .flavor-note {
    position: absolute; left: 0; right: 0; top: 880px; text-align: center;
    font-weight: 600; font-size: 48px; color: var(--ink);
  }
  .spec-pill {
    position: absolute; left: 172px; top: 984px; width: 688px; height: 76px;
    border-radius: 38px; background: var(--brand-green);
    display: flex; align-items: center; justify-content: center; gap: 14px;
    color: #fff; font-weight: 700; font-size: 27px;
  }
  .spec-divider { width: 2px; height: 40px; background: #fff; }
  .base-band {
    position: absolute; left: 0; right: 0; top: 1090px; height: 60px;
    background: linear-gradient(90deg, var(--brand-green) 0%, var(--brand-green-light) 30%, var(--brand-green) 55%, var(--brand-green) 100%);
  }
</style>
</head>
<body>
  <main class="label">
    <div class="texture-field" role="img" aria-label="Soft dotted halftone pattern in pale green"></div>

    <header class="brand-tab">
      <span class="brand-name">TIDELINE VIGOR</span>
    </header>

    <span class="vitamin vitamin-a">A</span>
    <span class="vitamin vitamin-fe">Fe</span>
    <span class="vitamin vitamin-e">E</span>
    <span class="vitamin vitamin-b">B</span>

    <h1 class="product-name">VEGAN</h1>

    <div class="athlete-figure" role="img" aria-label="Green silhouette of a running athlete"></div>

    <p class="flavor">CHOCOLATE MILKSHAKE</p>
    <p class="flavor-note">Natural Flavor</p>

    <div class="spec-pill">
      <span>NET WT. 907 G (2 LB)</span>
      <span class="spec-divider"></span>
      <span>DIETARY SUPPLEMENT</span>
    </div>

    <div class="base-band"></div>
  </main>
</body>
</html>
```